Business Stationery Design

I would like to get some stationery designed for my company. The stationery should include a letterhead, envelope, and business card. We are a technology consulting company specializing in Healthcare IT, and Education management systems. The colors of the stationery should match the logo. The logo is uploaded.

Target Market(s)

Hospitals, Clinics. Doctors offices. Private Schools.

Industry/Entity Type

Business

```html
<!DOCTYPE html>
<html lang="en">
<head>
<meta charset="utf-8">
<title>Oakwell Advisory Group – Stationery</title>
<link href="https://fonts.googleapis.com/css2?family=Montserrat:wght@400;500;600;700&display=swap" rel="stylesheet">
<style>
  :root{
    --green:#7bc043;
    --green-dark:#6aae35;
    --yellow:#f6b800;
    --paper:#f7f7f7;
    --bg:#e9e9e9;
    --ink:#4a4a4a;
    --ink-soft:#6b6b6b;
    --white:#ffffff;
  }
  *{box-sizing:border-box;margin:0;padding:0}
  html,body{width:1200px;height:605px;overflow:hidden}
  body{background:var(--bg);font-family:"Montserrat",sans-serif;color:var(--ink);position:relative}
  .piece{position:absolute;background:var(--paper);box-shadow:0 1px 3px rgba(0,0,0,.12);overflow:hidden}
  .piece svg.shape{position:absolute;left:0;top:0}
  .wordmark{font-weight:600;color:var(--green);letter-spacing:-.2px;line-height:1;white-space:nowrap;display:flex;align-items:center;gap:4px}
  .wordmark .dot{width:.7em;height:.7em;border-radius:50%;background:var(--yellow);flex:none}
  .wordmark.on-green{color:var(--white)}
  .contact{font-size:4.6px;line-height:1.5;color:var(--white)}
  .contact-line{display:flex;align-items:center;gap:3px}
  .icon{width:5px;height:5px;flex:none}
  .art{position:absolute}

  /* business card front */
  .card-front{left:58px;top:48px;width:154px;height:86px}
  .card-front .person{position:absolute;left:12px;top:21px}
  .card-front .name{font-size:7px;font-weight:700;color:var(--green)}
  .card-front .role{font-size:4.6px;color:var(--ink-soft);margin-top:2px;letter-spacing:.3px}
  .card-front .wordmark{position:absolute;right:12px;top:26px;font-size:7px}
  .card-front .band{position:absolute;left:0;bottom:0;width:100%;height:28px;background:var(--green);border-top:3px solid var(--yellow)}
  .card-front .band .addr{position:absolute;left:11px;top:6px}
  .card-front .band .tel{position:absolute;left:87px;top:6px}

  /* business card back */
  .card-back{left:241px;top:48px;width:154px;height:86px;background:var(--green)}
  .card-back .wordmark{position:absolute;left:50%;top:36px;transform:translateX(-50%);font-size:10px}
  .card-back .web{position:absolute;left:0;right:0;bottom:9px;text-align:center;font-size:4.4px;color:var(--white)}

  /* envelope back */
  .env-back{left:26px;top:158px;width:369px;height:188px}
  .env-back .wordmark{position:absolute;left:50%;top:126px;transform:translateX(-50%);font-size:12px}

  /* envelope front */
  .env-front{left:26px;top:371px;width:369px;height:189px}
  .env-front .sender{position:absolute;left:202px;top:14px;color:var(--white)}
  .env-front .sender .name{font-size:7.5px;font-weight:600}
  .env-front .sender .role{font-size:5px;margin:1px 0 7px}
  .env-front .sender .addr{font-size:5px;font-weight:500;line-height:1.45}
  .env-front .reach{position:absolute;left:284px;top:15px}
  .env-front .reach .contact{font-size:5px}
  .env-front .web-strip{position:absolute;left:284px;top:41px;width:85px;height:10px;background:var(--yellow);color:var(--white);font-size:5px;font-weight:600;padding:2px 0 0 4px}
  .env-front .art{left:0;top:95px;width:185px;height:94px;background:radial-gradient(ellipse at 45% 70%,#8fcd5c 0%,#b7e096 55%,rgba(247,247,247,0) 80%)}

  /* letterhead */
  .letterhead{left:422px;top:48px;width:364px;height:512px}
  .letterhead .wordmark{position:absolute;left:50%;top:78px;transform:translateX(-50%);font-size:12px}
  .letter{position:absolute;left:37px;top:146px;width:290px;font-size:5.9px;line-height:8.9px;color:var(--ink-soft);text-align:justify;text-align-last:center}
  .letter .greeting{font-size:8.5px;color:var(--ink);text-align:center;margin-bottom:18px}
  .letter p{margin-bottom:8.9px}
  .letter .signoff{text-align:center;margin-top:30px}
  .letterhead .footer{position:absolute;left:11px;top:470px;width:341px;height:29px;background:var(--green);border-bottom:3px solid var(--yellow)}
  .letterhead .footer .addr{position:absolute;left:8px;top:7px;font-size:5px}
  .letterhead .footer .tel{position:absolute;left:246px;top:7px;font-size:5px}

  /* presentation folder */
  .folder{left:811px;top:50px;width:365px;height:510px}
  .folder .art{left:0;top:205px;width:260px;height:305px;background:radial-gradient(ellipse at 45% 40%,#86c84f 0%,#a9d982 45%,rgba(247,247,247,0) 75%)}
</style>
</head>
<body>

<!-- business card front -->
<section class="piece card-front">
  <div class="person">
    <div class="name">Name Surname</div>
    <div class="role">POSITION</div>
  </div>
  <div class="wordmark">Oakwell</div>
  <div class="band">
    <div class="contact addr">0000 Main Street, Ste. 000<br>City name, NY 00000</div>
    <div class="contact tel">
      <div class="contact-line"><svg class="icon" viewBox="0 0 10 10"><circle cx="5" cy="5" r="5" fill="#fff"/><path d="M3.2 2.6l1 1-.5.7c.4.8 1 1.4 1.8 1.8l.7-.5 1 1-.7.8C4.9 7.2 2.8 5.1 2.6 3.3z" fill="#7bc043"/></svg>000-110-2200</div>
      <div class="contact-line"><svg class="icon" viewBox="0 0 10 10"><rect x="1" y="2.5" width="8" height="5" fill="#fff"/><path d="M1 2.5l4 3 4-3" stroke="#7bc043" stroke-width=".8" fill="none"/></svg>office@oakwelladvisory.com</div>
    </div>
  </div>
</section>

<!-- business card back -->
<section class="piece card-back">
  <div class="wordmark on-green">Oakwell</div>
  <div class="web">www.oakwelladvisory.com</div>
</section>

<!-- envelope back -->
<section class="piece env-back">
  <svg class="shape" width="369" height="188" viewBox="0 0 369 188">
    <path d="M0 0H369L356 24Q350 32 338 34L184 56L31 34Q19 32 13 24Z" fill="var(--green)"/>
  </svg>
  <div class="wordmark">Oakwell</div>
</section>

<!-- envelope front -->
<section class="piece env-front">
  <svg class="shape" width="369" height="189" viewBox="0 0 369 189">
    <path d="M0 0H369V58H205C140 58 60 62 0 80Z" fill="var(--green)"/>
    <path d="M0 44C90 28 190 60 230 140C180 72 100 50 0 54Z" fill="var(--yellow)"/>
  </svg>
  <div class="art" role="img" aria-label="Leafy branch artwork in brand green"></div>
  <div class="sender">
    <div class="name">Name Surname</div>
    <div class="role">Position</div>
    <div class="addr">0000 Main Street, Ste. 000<br>City name, NY 00000</div>
  </div>
  <div class="reach">
    <div class="contact">
      <div class="contact-line"><svg class="icon" viewBox="0 0 10 10"><circle cx="5" cy="5" r="5" fill="#fff"/><path d="M3.2 2.6l1 1-.5.7c.4.8 1 1.4 1.8 1.8l.7-.5 1 1-.7.8C4.9 7.2 2.8 5.1 2.6 3.3z" fill="#7bc043"/></svg>000-110-2200</div>
      <div class="contact-line"><svg class="icon" viewBox="0 0 10 10"><rect x="1" y="2.5" width="8" height="5" fill="#fff"/><path d="M1 2.5l4 3 4-3" stroke="#7bc043" stroke-width=".8" fill="none"/></svg>office@oakwelladvisory.com</div>
    </div>
  </div>
  <div class="web-strip">www.oakwelladvisory.com</div>
</section>

<!-- letterhead -->
<section class="piece letterhead">
  <div class="wordmark">Oakwell</div>
  <div class="letter">
    <div class="greeting">Dear Client,</div>
    <p>Harum faccumquam quidel et, si deris am, sant is repro et qui consequ atibusda nem ulpa velitius utatur, odi ut ut quoditi oratem quam exceria nobis et lit am. utem et laborer chillit, torestisit quundemporum aut magnis et latur sinvellanis quiaeperum quae lam etur sam escidestium diaecto estisque lam, am qui ipidignisin perum laborro optis repro et qui consequ atibusda nem ulpa velitius utatur, odi ut ut quoditi oratem quam ero iur, volupta dolorru mquatem rerum fugitatio. Nam lanis voluptatis suscipsa dolorehenis est quuntota sim intia porende ndant, to iur? Quis dem eum quatur solum qui int latur?<br>urio quam reste nullaborata animusam, omni necatet que plaudae porepudae sit alia pero iur, volupta dolorru mquatem rerum fugitatio. Nam lanis voluptatis suscipsa dolorehenis est quuntota sim intia porende ndant, to iur? Quis dem eum quatur solum qui int latur?</p>
    <p>Tem volupta volorehenim quiatio vendese quistio. Ullabor abore, ut ut volluptat odipsandust, consequ isquatione nia num res solum doluptas et, ne ped eumquia ndebitia nos repratquibus doluptatia quae odipsame voluptas et utatem que vid quibus ratem nos verferume nit et accus iust, con nim sitation rem aut la ea corest, qui consene stotat.<br>Evenimilitem volesto officiliciis sequisc iducitaectus nihitis aut ipsae doluptas dus deligendi quatur?</p>
    <p>Pid ma sintoriamus aut et, nem expliquam eum ide volum in eliamus eum fugitatiam ipis init auteni officiis vent dolorio quodis andiorest veres dis quasper umquibust, ommolup turescimpe qui beriossecto.</p>
    <div class="signoff">Sincerely,<br>Name Surname</div>
  </div>
  <div class="footer">
    <div class="contact addr">0000 Main Street, Ste. 000<br>City name, NY 00000</div>
    <div class="contact tel">
      <div class="contact-line"><svg class="icon" viewBox="0 0 10 10"><circle cx="5" cy="5" r="5" fill="#fff"/><path d="M3.2 2.6l1 1-.5.7c.4.8 1 1.4 1.8 1.8l.7-.5 1 1-.7.8C4.9 7.2 2.8 5.1 2.6 3.3z" fill="#7bc043"/></svg>000-110-2200</div>
      <div class="contact-line"><svg class="icon" viewBox="0 0 10 10"><rect x="1" y="2.5" width="8" height="5" fill="#fff"/><path d="M1 2.5l4 3 4-3" stroke="#7bc043" stroke-width=".8" fill="none"/></svg>office@oakwelladvisory.com</div>
    </div>
  </div>
</section>

<!-- presentation folder -->
<section class="piece folder">
  <svg class="shape" width="365" height="510" viewBox="0 0 365 510">
    <rect width="365" height="510" fill="var(--green)"/>
    <path d="M0 94C150 80 320 170 365 330V510H0Z" fill="var(--paper)"/>
    <path d="M0 112C160 96 320 190 350 322C300 220 160 136 0 138Z" fill="var(--yellow)"/>
  </svg>
  <div class="art" role="img" aria-label="Large leafy branch artwork in brand green"></div>
</section>

</body>
</html>
```